Awesome Business Card Design needed!

Hey there.
I'm looking for a simple but awesome business card design.
Type of company: Online advertisement agency
(please don't use the typical business people or statistics images on the card)
The front has to display the business name
and possibly some sort of logo ( perhaps something with the two M's of the biz name )
And the back of the card should say:
Name
Phone
Email
Let your imagination flow.
here are some designs that I like and that you can use as inspiration.
Simple but Awesome
http://images.pixelvantor.net/designs/55128_877673_43091_thumbnail.jpg
http://images.pixelvantor.net/designs/37714_747642_40106_image.jpg
http://images.pixelvantor.net/designs/55128_877673_43091_image.jpg
http://images.pixelvantor.net/designs/51321_781878_43091_image.jpg
http://images.pixelvantor.net/designs/33378_399063_15912_image.jpg
http://images.pixelvantor.net/designs/2337_271604_9495_image.jpg
good luck

```html
<!DOCTYPE html>
<html lang="en">
<head>
<meta charset="utf-8">
<title>Corvina Media – Business Card</title>
<link rel="stylesheet" href="https://fonts.googleapis.com/css2?family=PT+Sans:wght@400&display=swap">
<style>
  :root {
    --backdrop: #d6d6d6;
    --card: #000000;
    --label: #8c8c8c;
    --ink: #ffffff;
    --mark: #262626;
  }

  * { margin: 0; padding: 0; box-sizing: border-box; }

  html, body {
    width: 1200px;
    height: 750px;
    overflow: hidden;
  }

  body {
    background: var(--backdrop);
    font-family: "PT Sans", sans-serif;
  }

  .card-sheet {
    position: relative;
    width: 1200px;
    height: 750px;
  }

  .card {
    position: absolute;
    top: 230px;
    width: 520px;
    height: 290px;
    background: var(--card);
    overflow: hidden;
  }

  .card--back  { left: 60px; }
  .card--front { left: 620px; }

  /* Back: large faint brand name as decoration */
  .brand-watermark {
    position: absolute;
    right: 30px;
    bottom: 26px;
    color: var(--mark);
    font-size: 64px;
    line-height: 1;
    white-space: nowrap;
  }

  .contact-list {
    list-style: none;
    position: absolute;
    left: 36px;
    top: 32px;
    color: var(--label);
    font-size: 33px;
    line-height: 52px;
  }

  /* Front: plain square standing where the mark sits */
  .brand-block {
    position: absolute;
    left: 170px;
    top: 62px;
    width: 180px;
    height: 180px;
    background: var(--mark);
  }

  .brand {
    position: absolute;
    left: 0;
    right: 0;
    top: 128px;
    text-align: center;
    color: var(--ink);
  }

  .brand__name {
    display: inline-block;
    font-size: 52px;
    font-weight: 400;
    line-height: 1;
    padding-bottom: 4px;
    border-bottom: 3px solid var(--ink);
  }

  .brand__tagline {
    margin-top: 8px;
    font-size: 27px;
    line-height: 1;
  }
</style>
</head>
<body>
  <main class="card-sheet">
    <section class="card card--back" aria-label="Card back">
      <span class="brand-watermark" aria-hidden="true">Corvina Media</span>
      <ul class="contact-list">
        <li>Name</li>
        <li>Phone</li>
        <li>Email</li>
      </ul>
    </section>

    <section class="card card--front" aria-label="Card front">
      <div class="brand-block" aria-hidden="true"></div>
      <div class="brand">
        <h1 class="brand__name">Corvina Media</h1>
        <p class="brand__tagline">online advertisement agency</p>
      </div>
    </section>
  </main>
</body>
</html>
```